Poster Design for Photography Exhibit

We are looking for a poster design for a photography exhibit featuring high-end fashion and celebrity photography.

Name of the exhibit is "TOBIAS WRENLEY: AFTERGLOW" (please use Helvetica Black all cap for show name.

Poster is LANDSCAPE format (2 units wide by 1 unit high).

Unfortunately due to legal reasons, we cannot use any actual Tobias Wrenley photos. No can we use fashions or people on the poster!

We are looking for a high-end, sexy, bold provocative design that captures the excitement and glamour of a fashion photo shoot.

Target Market(s)

Men and Women interested in Fashion Photography and art photography in general

Industry/Entity Type

Fashion

Requirements
Must have
• landscape format, name of exhibit in Helvetica Black all caps
Nice to have
• Can be grayscale or color.
Should not have
• Logos or brand names

```html
<!DOCTYPE html>
<html lang="en">
<head>
<meta charset="utf-8">
<title>Tobias Wrenley : Afterglow</title>
<link rel="stylesheet" href="https://fonts.googleapis.com/css2?family=Archivo+Black&display=swap">
<style>
  :root {
    --page: #ffffff;
    --band: #000000;
    --title: #d3d8b6;
    --spot-centre: #ffffff;
    --spot-mid: #eef0e2;
    --spot-edge: #c7cfa6;
  }
  html, body {
    margin: 0;
    padding: 0;
    width: 1200px;
    height: 900px;
    overflow: hidden;
    background: var(--page);
  }
  .poster {
    position: absolute;
    left: 55px;
    top: 178px;
    width: 1092px;
    height: 546px;
    display: block;
  }
  .poster-band { fill: var(--band); }
  .spotlight-stop-centre { stop-color: var(--spot-centre); }
  .spotlight-stop-mid { stop-color: var(--spot-mid); }
  .spotlight-stop-edge { stop-color: var(--spot-edge); }
  .exhibit-title {
    font-family: "Archivo Black", "Helvetica Neue", Helvetica, Arial, sans-serif;
    font-size: 60px;
    fill: var(--title);
    text-transform: uppercase;
  }
</style>
</head>
<body>
  <svg class="poster" viewBox="0 0 1092 546" xmlns="http://www.w3.org/2000/svg">
    <defs>
      <radialGradient id="spotlight-glow" cx="0.62" cy="0.62" r="0.6">
        <stop offset="0" class="spotlight-stop-centre"/>
        <stop offset="0.45" class="spotlight-stop-mid"/>
        <stop offset="1" class="spotlight-stop-edge"/>
      </radialGradient>
    </defs>
    <rect class="poster-band" x="0" y="0" width="1092" height="546"/>
    <circle class="spotlight-photo" cx="370" cy="104" r="301" fill="url(#spotlight-glow)"
            role="img" aria-label="Spotlit studio photograph: legs in black leggings and high-heeled shoes perched on a black bar stool"/>
    <text class="exhibit-title" x="47" y="489" textLength="1000" lengthAdjust="spacingAndGlyphs">TOBIAS WRENLEY : AFTERGLOW</text>
  </svg>
</body>
</html>
```